A5 Leaflet for attracting new custom to our scrap yard

My company is called Harrowfield Metal Traders, the company buys scrap metal from domestic customers, plumbers, electricians, roofers, fabrication companies, demolition companies etc etc
We are looking for a leaflet that is double sided, with various different elements needed, it must be eye catching not too busy , straight to the point it must appeal to both our door trade customers such as plumbers, electricians, roofers etc and also must appeal to our bigger customers such as the large fabrication companies and in particular it must push our new skip service facility. The overall aim of the leaflet is to raise awareness to new customers that we exist and pay some of the best prices around for scrap metal, that we offer excellent service, skip service available, a map of where our industrial unit is, our logo and company name, must include telephone number, mobile number , web address, and also must emphasis they can now connect via Facebook, linked in and twitter and opening times. As well as advising the customers we pay excellent prices for copper, brass, stainless steel, batteries, household wire etc we now offer excellent prices for steel, cast iron and new steel cuttings. Our company colour is green as per our logo and we would like that to feature quite heavily, some eye catching pictures of the scrap metal we buy should be included in particular on the front of the flyer, on the back we would like our map to feature and also a picture of all our wagons in front of our unit on the back with a similar tag line like "we are ready when you are"

our opening times are monday to friday 8am to 5pm and saturday from 9am to 12pm

we are a family run business with family values and the aim of this leaflet is to attract new customers, encouraging them to us again or perhaps for the first time, the back of the leaflet should also include a picture of our new skip loader and should advise the customer that skips from 2yard to 40yards can be dropped onsite . We serve all local areas them being Burnley, Padiham, Nelson, Colne, Barnoldswick, Earby, Clitheroe, Skipton and Accrington
Finally should also include our address of course
Updates

Project Deadline Extended
Reason: as i have not long uploaded my pictures and further information i have extended by two days

Project Deadline Extended
Reason: extended for last minute designs and re submits thanks

Project Deadline Extended

Project Deadline Extended

Target Market(s)

website address : www.harrowfieldmetaltraders.co.uk

Industry/Entity Type

Industrial

```html
<!DOCTYPE html>
<html lang="en">
<head>
<meta charset="utf-8">
<title>Harrowfield Metal Traders – Leaflet</title>
<link rel="stylesheet" href="https://fonts.googleapis.com/css2?family=Anton&family=Roboto:wght@300;400&display=swap">
<style>
  :root {
    --green: #1fc70f;
    --black: #000000;
    --white: #ffffff;
    --grey-text: #444444;
    --rule-grey: #9a9a9a;
    --copper: #b8643a;
    --wire: #a9acae;
    --rust: #5d4634;
    --battery: #3a3a38;
    --truck: #8a8f8c;
  }
  * { margin: 0; padding: 0; box-sizing: border-box; }
  html, body { width: 864px; height: 1200px; overflow: hidden; background: var(--white); }
  .leaflet { position: relative; width: 864px; height: 1200px; background: var(--white); font-family: "Roboto", Arial, sans-serif; }
  .frame { position: absolute; left: 36px; top: 36px; width: 792px; height: 1118px; background: var(--black); border: 4px solid var(--black); border-radius: 3px; }
  .abs { position: absolute; }

  .brand-panel { left: 42px; top: 42px; width: 478px; height: 384px; background: var(--green); }
  .brand-title { position: absolute; left: 100px; top: 80px; width: 294px; text-align: center; font-family: "Anton", Impact, sans-serif; font-weight: 400; line-height: 1; text-transform: uppercase; }
  .brand-title .main { display: block; font-size: 58px; color: var(--black); letter-spacing: -0.5px; }
  .brand-title .sub { display: block; font-size: 52px; color: var(--white); margin-top: 4px; line-height: 0.98; }
  .brand-rule { position: absolute; left: 100px; top: 281px; width: 294px; height: 2px; background: var(--white); }
  .brand-tagline { position: absolute; left: 100px; top: 289px; width: 294px; text-align: center; font-size: 23px; font-weight: 300; color: var(--white); letter-spacing: 0.3px; }

  .photo-wheels { left: 526px; top: 42px; width: 198px; height: 246px; background: linear-gradient(160deg, #c9cbcd, #77797c 60%, #3e3f41); }
  .photo-pipes { left: 526px; top: 293px; width: 198px; height: 133px; background: linear-gradient(135deg, #d49a74, var(--copper) 55%, #6b3b25); }

  .web-strip { left: 730px; top: 42px; width: 93px; height: 474px; background: var(--green); }
  .web-address { position: absolute; left: 50%; top: 14px; transform: translateX(-50%) rotate(180deg); writing-mode: vertical-rl; font-size: 16px; color: var(--white); font-weight: 300; letter-spacing: 0.2px; }

  .photo-wagons { left: 730px; top: 524px; width: 93px; height: 78px; background: linear-gradient(180deg, #cfd4d6, var(--truck) 55%, #b23a30 56%, #6e6f6e); }
  .photo-offcuts { left: 730px; top: 644px; width: 93px; height: 40px; background: linear-gradient(90deg, #7d7f82, #c3c5c7, #7d7f82); }

  .intro { left: 94px; top: 472px; width: 560px; font-size: 17.5px; line-height: 22.5px; color: var(--white); font-weight: 400; }

  .photo-wire { left: 40px; top: 688px; width: 184px; height: 166px; background: linear-gradient(135deg, #d9dbdc, var(--wire) 50%, #6b6e70); }
  .photo-motors { left: 229px; top: 688px; width: 302px; height: 166px; background: linear-gradient(135deg, #8a7a64, var(--rust) 55%, #2c2520); }
  .photo-copper-wire { left: 536px; top: 688px; width: 287px; height: 166px; background: linear-gradient(135deg, #e2a27c, var(--copper) 55%, #7b3a1f); }
  .photo-batteries { left: 156px; top: 859px; width: 186px; height: 170px; background: linear-gradient(160deg, #9a9a92, var(--battery) 55%, #1b1b1a); }

  .opening-times { left: 398px; top: 910px; width: 380px; text-align: center; font-size: 18px; line-height: 22px; text-transform: uppercase; color: var(--green); }
  .opening-times .lead { color: var(--white); }

  .footer { left: 40px; top: 1030px; width: 783px; height: 120px; background: var(--white); }
  .footer-address { position: absolute; left: 40px; top: 40px; width: 488px; text-align: center; font-size: 13.5px; color: var(--grey-text); }
  .footer-contact { position: absolute; left: 40px; top: 74px; width: 488px; text-align: center; font-size: 13px; color: var(--green); }
  .footer-contact .sep { color: var(--grey-text); }
  .footer-divider { position: absolute; left: 528px; top: 28px; width: 1px; height: 70px; background: var(--rule-grey); }
  .footer-brand { position: absolute; left: 552px; top: 44px; display: flex; align-items: center; gap: 8px; }
  .footer-brand .dot { width: 34px; height: 34px; border-radius: 50%; background: var(--green); flex: none; }
  .footer-brand .name { font-family: "Anton", Impact, sans-serif; font-size: 17px; line-height: 1.05; color: var(--green); text-transform: uppercase; width: 170px; }
</style>
</head>
<body>
<div class="leaflet">
  <div class="frame"></div>

  <section class="abs brand-panel">
    <h1 class="brand-title">
      <span class="main">Harrowfield</span>
      <span class="sub">Metal</span>
      <span class="sub">Traders</span>
    </h1>
    <div class="brand-rule"></div>
    <p class="brand-tagline">SCRAP METAL DEALERS</p>
  </section>

  <div class="abs photo-wheels" role="img" aria-label="Photo of scrap alloy car wheels"></div>
  <div class="abs photo-pipes" role="img" aria-label="Photo of scrap copper pipes"></div>

  <aside class="abs web-strip">
    <span class="web-address">www.harrowfieldmetaltraders.co.uk</span>
  </aside>

  <div class="abs photo-wagons" role="img" aria-label="Photo of company wagons parked in front of the unit"></div>
  <div class="abs photo-offcuts" role="img" aria-label="Photo of metal turnings and offcuts"></div>

  <p class="abs intro">We are a family run business with family values, paying some of the best prices around for copper, brass, stainless steel, batteries, household wire, steel, cast iron and new steel cuttings. Our new skip service drops skips from 2 yards to 40 yards onsite – we are ready when you are. We serve Burnley, Padiham, Nelson, Colne, Barnoldswick, Earby, Clitheroe, Skipton and Accrington. Connect with us on social media today.</p>

  <div class="abs photo-wire" role="img" aria-label="Photo of scrap household wire"></div>
  <div class="abs photo-motors" role="img" aria-label="Photo of scrap electric motors"></div>
  <div class="abs photo-copper-wire" role="img" aria-label="Photo of bundled copper wire"></div>
  <div class="abs photo-batteries" role="img" aria-label="Photo of scrap car batteries"></div>

  <p class="abs opening-times"><span class="lead">Our opening times are Monday</span><br>to Friday 8am to 5pm and<br>Saturday from 9am to 12pm</p>

  <footer class="abs footer">
    <p class="footer-address">Unit 4 Fellside Works, Kiln Brook Lane, Burnley, Lancashire. BB11 9ZZ</p>
    <p class="footer-contact">T: 01632 960 118 <span class="sep">|</span> M: 07700 900 600 <span class="sep">| E: info@harrowfieldmetaltraders.co.uk</span></p>
    <div class="footer-divider"></div>
    <div class="footer-brand">
      <span class="dot"></span>
      <span class="name">Harrowfield Metal Traders</span>
    </div>
  </footer>
</div>
</body>
</html>
```